Business Card for Language School (2 locations)

We need a sleek business card for a language school that is looking to update our image to be more professional. We work with students ages Pre-Kindergarten through adults. Our idea is to have an all-black business card with white or silver lettering. On the front will be the name of our school (Bright Maple English Academy), and on the back there will be information for our location, phone number, email, and website (and possibly social media information). We have two school branches, so the address, phone number, and email address will be different for each branch, but all of the other information will stay the same. We'd like each branch to have a different color card edge that is neon. We are also open to suggestions and new ideas!

Some answers to questions we have received:
1. The reason we haven't added a logo is because we are looking to get a new one. We hadn't originally planned to do that at this time, but we are going to look into updating our project to include that as another aspect of it. We had previously planned to just include the school name on the front without a logo at this time.
2. We currently have two branches of our school, and we want our business card design to be uniform for each location. While it might make sense to put the information on one card right now, we plan to have more locations in the future, so we want to plan ahead with a unified design right now.
3. Our school addresses and phone numbers can be found on our website: www.brightmapleenglish.example (at the bottom of the page)!
Updates

Part of this contest is also a new logo design. Our previous design was a train, which we would be open to keeping if it had an updated, sleeker design.

Contact Information for Business Card

Card #1:
Bright Maple English Academy (Qiaolin Branch)
Yuqing W. Rd. Sec. 3, Lane 412, No. 29, 1F
Beitou District, Taipei City 11268
02-2649-3058
qiaolin@brightmapleenglish.example

Card #2:
Bright Maple English Academy (Fenghe Branch)
Fulan Road, No. 318, 1F
Songshan District, Taipei City 10573
02-2761-4402
fenghe@brightmapleenglish.example

Both cards:
Website: www.brightmapleenglish.example
Facebook: www.facebook.com/brightmapleenglish
Instagram: @brightmapleenglish

```html
<!DOCTYPE html>
<html lang="en">
<head>
<meta charset="utf-8">
<title>Bright Maple English Academy – Business Card</title>
<link href="https://fonts.googleapis.com/css2?family=Jost:wght@400;500&display=swap" rel="stylesheet">
<style>
  :root {
    --backdrop: #111111;
    --card: #1d1d1d;
    --card-edge: #262626;
    --emboss: #3e3e3e;
    --silver: #d6d6d6;
    --white: #f2f2f2;
    --mark: #2c2c2c;
  }
  * { margin: 0; padding: 0; box-sizing: border-box; }
  html, body { width: 1200px; height: 900px; overflow: hidden; background: var(--backdrop); }
  body { position: relative; font-family: "Jost", sans-serif; }

  .card {
    position: absolute;
    left: 290px;
    width: 620px;
    height: 354px;
    background: var(--card);
    border: 1px solid var(--card-edge);
    overflow: hidden;
  }
  .card--front { top: 60px; }
  .card--back { top: 470px; }

  .wordmark {
    position: absolute;
    display: flex;
    align-items: center;
    gap: 26px;
  }
  .wordmark__square { background: var(--mark); flex: none; }
  .wordmark__name {
    color: var(--silver);
    font-weight: 500;
    line-height: 1.05;
    white-space: nowrap;
  }
  .card--front .wordmark { left: 170px; top: 112px; }
  .card--front .wordmark__square { width: 92px; height: 92px; }
  .card--front .wordmark__name { font-size: 38px; }

  .card--back .wordmark { right: 40px; top: 112px; gap: 16px; }
  .card--back .wordmark__square { width: 56px; height: 56px; }
  .card--back .wordmark__name { font-size: 24px; }

  .branch {
    position: absolute;
    left: 40px;
    top: 36px;
    color: var(--emboss);
    font-size: 20px;
    font-weight: 500;
    line-height: 1.2;
    white-space: nowrap;
  }
  .address {
    position: absolute;
    left: 40px;
    top: 118px;
    color: var(--emboss);
    font-size: 19px;
    line-height: 1.3;
    white-space: nowrap;
  }
  .contact {
    position: absolute;
    left: 40px;
    top: 228px;
    list-style: none;
    color: var(--emboss);
    font-size: 17px;
    line-height: 1.4;
    white-space: nowrap;
  }
  .contact li { display: flex; align-items: center; gap: 10px; }
  .contact svg { width: 12px; height: 12px; flex: none; }

  .social {
    position: absolute;
    right: 32px;
    bottom: 34px;
    color: var(--white);
    font-size: 18px;
    line-height: 1.35;
    white-space: nowrap;
  }
  .social b { font-weight: 500; }
</style>
</head>
<body>

<section class="card card--front" aria-label="Card front">
  <div class="wordmark">
    <span class="wordmark__square"></span>
    <p class="wordmark__name">Bright Maple<br>English<br>Academy</p>
  </div>
</section>

<section class="card card--back" aria-label="Card back">
  <p class="branch">Bright Maple English Academy<br>(Qiaolin Branch)</p>
  <p class="address">Yuqing W. Rd. Sec. 3,<br>Lane 412, No. 29, 1F<br>Beitou District, Taipei City 11268</p>
  <ul class="contact">
    <li>
      <svg viewBox="0 0 16 16" aria-hidden="true"><path d="M4 1l3 3-2 2c1 2 3 4 5 5l2-2 3 3-2 2C7 14 2 9 2 3z" fill="currentColor"/></svg>
      02-2649-3058
    </li>
    <li>
      <svg viewBox="0 0 16 16" aria-hidden="true"><rect x="1.5" y="3.5" width="13" height="9" fill="none" stroke="currentColor" stroke-width="1.5"/><path d="M1.5 3.5l6.5 5 6.5-5" fill="none" stroke="currentColor" stroke-width="1.5"/></svg>
      qiaolin@brightmapleenglish.example
    </li>
    <li>
      <svg viewBox="0 0 16 16" aria-hidden="true"><circle cx="8" cy="8" r="6.5" fill="none" stroke="currentColor" stroke-width="1.5"/><path d="M1.5 8h13M8 1.5c-3 3.5-3 9.5 0 13M8 1.5c3 3.5 3 9.5 0 13" fill="none" stroke="currentColor" stroke-width="1.2"/></svg>
      www.brightmapleenglish.example
    </li>
  </ul>
  <div class="wordmark">
    <span class="wordmark__square"></span>
    <p class="wordmark__name">Bright Maple<br>English<br>Academy</p>
  </div>
  <p class="social"><b>Fb:</b> /brightmapleenglish<br><b>Ins:</b> @brightmapleenglish</p>
</section>

</body>
</html>
```